R&T Builders and Spaces Business Card

We need to redesign our business card. We had used white vellum wih grey logo and txt in the past. I would like to bring a little life into our cards without being over the top. I think I will be going away from the vellum and printing soft touch business cards.
I have attached what we currently have and our new logo design.

```html
<!DOCTYPE html>
<html lang="en">
<head>
<meta charset="utf-8">
<title>R&amp;T Builders and Spaces – Business Card</title>
<link rel="stylesheet" href="https://fonts.googleapis.com/css2?family=Source+Sans+3:wght@400;700&display=swap">
<style>
  :root {
    --page: #f1f1f1;
    --paper: #ffffff;
    --charcoal: #3a3a3c;
    --ink: #3d3d3d;
    --inverse: #ffffff;
  }
  * { margin: 0; padding: 0; box-sizing: border-box; }
  html, body { width: 1199px; height: 1200px; overflow: hidden; }
  body {
    background: var(--page);
    font-family: "Source Sans 3", "Source Sans Pro", Arial, sans-serif;
    color: var(--ink);
    position: relative;
  }
  .card {
    position: absolute;
    left: 165px;
    width: 869px;
    height: 512px;
    overflow: hidden;
  }
  .card--front { top: 69px; background: var(--paper); }
  .card--back { top: 621px; background: var(--charcoal); }

  .brand {
    position: absolute;
    display: flex;
    flex-direction: column;
    justify-content: flex-end;
    gap: 22px;
  }
  .brand__square { width: 64px; height: 64px; }
  .brand__name {
    font-weight: 400;
    text-transform: uppercase;
    letter-spacing: 3px;
    line-height: 1.25;
  }
  .card--front .brand { left: 79px; top: 79px; width: 239px; height: 239px; }
  .card--front .brand__square { background: var(--charcoal); }
  .card--front .brand__name { color: var(--charcoal); font-size: 24px; }

  .card--back .brand { left: 279px; top: 97px; width: 314px; height: 317px; gap: 28px; }
  .card--back .brand__square { width: 80px; height: 80px; background: var(--inverse); }
  .card--back .brand__name { color: var(--inverse); font-size: 31px; }

  .person { position: absolute; left: 467px; top: 72px; }
  .person__name { font-size: 36px; font-weight: 700; letter-spacing: 0.5px; line-height: 1.1; }
  .person__title { font-size: 20px; font-weight: 400; margin-top: 6px; letter-spacing: 0.5px; }

  .contact { position: absolute; left: 471px; top: 205px; list-style: none; font-size: 20px; line-height: 1; }
  .contact__item { display: flex; align-items: center; gap: 8px; height: 32px; }
  .contact__item--address { align-items: flex-start; margin-top: 30px; height: auto; line-height: 28px; }
  .contact__item--address .icon { margin-top: 6px; }
  .icon { width: 16px; height: 16px; flex: none; fill: var(--ink); }

  .band {
    position: absolute;
    left: 0; right: 0; top: 410px; height: 46px;
    background: var(--charcoal);
    color: var(--inverse);
    display: flex; align-items: center;
    padding-left: 471px;
    gap: 8px;
    font-size: 20px;
  }
  .band .icon { fill: var(--inverse); }
</style>
</head>
<body>
  <section class="card card--front">
    <div class="brand">
      <span class="brand__square"></span>
      <span class="brand__name">R&amp;T Builders and Spaces</span>
    </div>

    <div class="person">
      <h1 class="person__name">DALE M. HARLAN</h1>
      <p class="person__title">PRINCIPAL</p>
    </div>

    <ul class="contact">
      <li class="contact__item">
        <svg class="icon" viewBox="0 0 16 16"><path d="M3.6 1.5l2.3 2.8-1.4 1.8c.9 2 2.5 3.6 4.5 4.5l1.8-1.4 2.8 2.3-1.3 2.3C7 13.4 2.6 9 2.2 2.8z"/></svg>
        520 555 0148
      </li>
      <li class="contact__item">
        <svg class="icon" viewBox="0 0 16 16"><path d="M4.5 1h7v14h-7zM5.8 2.5v10h4.4v-10zM7.3 13.2h1.4v1h-1.4z" fill-rule="evenodd"/></svg>
        520 555 0173
      </li>
      <li class="contact__item">
        <svg class="icon" viewBox="0 0 16 16"><path d="M1 3.5h14v9H1zM1.8 4.2L8 9l6.2-4.8v-.2H1.8z"/></svg>
        DALEH@RTBUILDERS.COM
      </li>
      <li class="contact__item contact__item--address">
        <svg class="icon" viewBox="0 0 16 16"><path d="M8 1a4.5 4.5 0 014.5 4.5C12.5 9 8 12.5 8 12.5S3.5 9 3.5 5.5A4.5 4.5 0 018 1zm0 2.6a1.9 1.9 0 100 3.8 1.9 1.9 0 000-3.8zM2 13.5h12V15H2z" fill-rule="evenodd"/></svg>
        <span>4120 W MESA RIDGE RD, SUITE 210<br>TUCSON, ARIZONA 85705</span>
      </li>
    </ul>

    <div class="band">
      <svg class="icon" viewBox="0 0 16 16"><path d="M8 1a7 7 0 110 14A7 7 0 018 1zm-2 2.3C4 4.2 2.6 6 2.5 8.2h2.6c.1-1.9.4-3.6.9-4.9zm4 0c.5 1.3.8 3 .9 4.9h2.6c-.1-2.2-1.5-4-3.5-4.9zM6.3 8.2c.1 2.6.8 4.9 1.7 5.6.9-.7 1.6-3 1.7-5.6z" fill-rule="evenodd"/></svg>
      WWW.RTBUILDERS.COM
    </div>
  </section>

  <section class="card card--back">
    <div class="brand">
      <span class="brand__square"></span>
      <span class="brand__name">R&amp;T Builders and Spaces</span>
    </div>
  </section>
</body>
</html>
```